Re-design / re-work of existing website

Need to re-design a website so it's easy for me as a user to update/add pictures and change descriptions.

If possible, would there be a way to display LodgeVista calendars? We have 3 cottages and it would be ideal to have each cottage with pics on one page along with a readonly version of the LodgeVista calendar plugin (if such a thing exists) so that visitors to the site can see what is available and what is not.

Existing site: http://tarnwoodlets.net

```html
<!DOCTYPE html>
<html lang="en">
<head>
<meta charset="utf-8">
<title>Tarnwood Cottages</title>
<link href="https://fonts.googleapis.com/css2?family=Jost:wght@400;500;600&family=Montserrat:wght@600;700&family=Mrs+Saint+Delafield&display=swap" rel="stylesheet">
<style>
:root{
  --tan:#c5ae93;
  --tan-dark:#b59c7e;
  --tan-panel:rgba(180,158,128,.85);
  --ink:#111111;
  --body:#2b2b2b;
  --white:#ffffff;
  --black:#000000;
  --shadow:0 10px 30px rgba(0,0,0,.12);
}
*{margin:0;padding:0;box-sizing:border-box}
html,body{width:1200px;height:3911px;overflow:hidden;background:var(--white)}
body{position:relative;font-family:"Jost",sans-serif;color:var(--body)}
.abs{position:absolute}
.script{font-family:"Mrs Saint Delafield",cursive;color:var(--tan);font-weight:400;line-height:1}
.heading{font-family:"Montserrat",sans-serif;font-weight:700;color:var(--ink);text-transform:uppercase;letter-spacing:.5px}

/* header */
.site-header{left:0;top:0;width:1200px;height:115px;background:var(--white)}
.brand{left:144px;top:30px;width:180px;font-size:22px;font-weight:500;color:var(--ink);display:flex;align-items:center;gap:10px}
.brand-mark{width:14px;height:14px;border-radius:50%;background:var(--ink)}
.contact-bar{left:377px;top:0;width:744px;height:49px;background:var(--tan);clip-path:polygon(0 0,100% 0,97.5% 100%,2.5% 100%);clip-path:polygon(0 0,100% 0,97.8% 50%,100% 100%... );}
.contact-bar{clip-path:polygon(0 0,100% 0,97.8% 100%,2.2% 100%)}
.contact-bar ul{list-style:none;display:flex;gap:30px;height:100%;align-items:center;padding-left:48px;font-size:14px;color:var(--white)}
.contact-bar li{display:flex;align-items:center;gap:9px}
.main-nav{left:437px;top:74px;display:flex;gap:23px;font-size:14px;color:var(--ink)}
.main-nav a{color:inherit;text-decoration:none;position:relative}
.main-nav a.active::after{content:"";position:absolute;left:0;right:0;bottom:-26px;height:3px;background:var(--tan)}

/* hero */
.hero{left:0;top:115px;width:1200px;height:566px;background:linear-gradient(120deg,#6e604f 0%,#8a7a66 35%,#7d8a8c 65%,#5c554c 100%)}
.hero-eyebrow{left:111px;top:264px;font-family:"Montserrat",sans-serif;font-weight:600;font-size:26px;color:var(--tan);letter-spacing:.5px}
.hero-title{left:106px;top:290px;font-size:118px;color:var(--white)}
.btn{display:inline-flex;align-items:center;justify-content:center;background:var(--tan);color:var(--white);font-family:"Montserrat",sans-serif;font-weight:600;font-size:14px;text-transform:uppercase;border-radius:30px;text-decoration:none}
.hero-btn{left:111px;top:456px;width:162px;height:51px}

/* cottages */
.section-label{font-size:52px}
.cottages-label{left:0;width:1200px;text-align:center;top:765px}
.cottages-title{left:0;width:1200px;text-align:center;top:834px;font-size:34px}
.card{background:var(--white);border-radius:20px;overflow:hidden;box-shadow:var(--shadow)}
.cottage-card{top:927px;width:312px;height:390px}
.card-photo{width:100%;height:225px}
.card-body{padding:14px 21px}
.cottage-card h3{font-size:23px;font-weight:500;color:var(--ink);margin-bottom:10px}
.cottage-card p{font-size:16px;line-height:26px}
.text-link{display:inline-block;margin-top:6px;font-size:15px;font-weight:500;color:var(--tan);text-decoration:underline}

/* about */
.about-photo{left:0;top:1444px;width:547px;height:508px;border-radius:0 18px 18px 0;background:linear-gradient(160deg,#c9b79d 0%,#a57a4f 45%,#6d5a46 100%)}
.about-label{left:598px;top:1455px}
.about-title{left:600px;top:1518px;font-size:35px;line-height:41px}
.about-text{left:600px;top:1612px;width:492px;font-size:15.5px;line-height:25.7px;color:var(--ink)}
.about-btn{left:595px;top:1868px;width:160px;height:57px}

/* explore */
.explore-bg{left:640px;top:2063px;width:560px;height:726px;background:linear-gradient(180deg,#d8c9b3 0%,#c9b699 50%,#b9a283 100%)}
.explore-label{left:115px;top:2115px}
.explore-title{left:115px;top:2179px;font-size:36px;line-height:40px}
.explore-track{left:0;top:2300px;width:1200px;height:400px;overflow:hidden}
.place-card{top:12px;width:398px;height:366px;border-radius:0}
.place-card .card-photo{height:228px}
.place-card .card-body{padding:28px 33px}
.place-card h3{font-size:19px;font-weight:500;color:var(--ink);line-height:26px}
.place-card .text-link{font-size:13px;margin-top:12px}
.slider-arrows{left:662px;top:2740px;display:flex;gap:10px}

/* space */
.space-panel{left:330px;top:2941px;width:758px;height:308px;border-radius:30px;background:var(--tan-panel)}
.space-photo{left:97px;top:2880px;width:428px;height:428px;border-radius:50%;background:linear-gradient(170deg,#c9cfc4 0%,#6d5d4c 45%,#3d3630 75%,#8a847a 100%)}
.space-label{left:572px;top:2965px;font-size:42px;color:var(--white)}
.space-title{left:572px;top:3018px;font-size:36px;color:var(--white)}
.space-text{left:575px;top:3073px;width:490px;font-size:15.5px;line-height:25.7px;color:var(--white)}
.space-link{left:575px;top:3188px;font-family:"Montserrat",sans-serif;font-weight:600;font-size:14px;color:var(--white);text-decoration:underline}

/* footer */
.site-footer{left:0;top:3406px;width:1200px;height:505px;background:var(--black);color:var(--white)}
.footer-brand{left:0;width:1200px;top:155px;text-align:center;font-size:34px;font-weight:500}
.footer-nav{left:0;width:1200px;top:290px;display:flex;justify-content:center;gap:23px;font-size:14px}
.footer-nav a{color:var(--white);text-decoration:none}
.copyright{left:0;width:1200px;top:348px;text-align:center;font-size:13px}
.copyright a{color:var(--tan)}
.socials{left:501px;top:403px;display:flex;gap:7px}
.social{width:44px;height:44px;border-radius:50%;background:var(--white)}
.social.first{background:var(--tan)}
</style>
</head>
<body>

<header class="site-header abs">
  <div class="brand abs"><span class="brand-mark"></span>Tarnwood Cottages</div>
  <div class="contact-bar abs">
    <ul>
      <li><svg width="11" height="14" viewBox="0 0 11 14"><path d="M5.5 0A5.5 5.5 0 0 0 0 5.5C0 9.6 5.5 14 5.5 14S11 9.6 11 5.5A5.5 5.5 0 0 0 5.5 0Zm0 7.6a2.1 2.1 0 1 1 0-4.2 2.1 2.1 0 0 1 0 4.2Z" fill="#fff"/></svg>418 Tarnwood Bay Road, Birchmere K0L 2B0</li>
      <li><svg width="13" height="13" viewBox="0 0 24 24"><path d="M6.6 10.8a15.1 15.1 0 0 0 6.6 6.6l2.2-2.2c.3-.3.7-.4 1-.2 1.1.4 2.3.6 3.6.6.6 0 1 .4 1 1V20c0 .6-.4 1-1 1A17 17 0 0 1 3 4c0-.6.4-1 1-1h3.5c.6 0 1 .4 1 1 0 1.3.2 2.5.6 3.6.1.3 0 .7-.2 1l-2.3 2.2Z" fill="#fff"/></svg>+1 555 204 7713</li>
      <li><svg width="13" height="10" viewBox="0 0 13 10"><rect width="13" height="10" rx="1" fill="#fff"/><path d="M0.5 1l6 4.5 6-4.5" stroke="#c5ae93" fill="none"/></svg>support@tarnwoodlets.net</li>
    </ul>
  </div>
  <nav class="main-nav abs">
    <a class="active" href="#">Home</a><a href="#">Our Cottages</a><a href="#">Adventures</a><a href="#">Getting Here</a><a href="#">Contact Us</a><a href="#">Today’s Weather</a><a href="#">Policies</a>
  </nav>
</header>

<section>
  <div class="hero abs" role="img" aria-label="Bright cottage dining and living room with wooden table, pendant lights and lake-view windows"></div>
  <p class="hero-eyebrow abs">WELCOME TO</p>
  <h1 class="hero-title script abs">Tarnwood Cottages</h1>
  <a class="btn hero-btn abs" href="#">Get Started</a>
</section>

<section>
  <p class="section-label script cottages-label abs">Cottages</p>
  <h2 class="heading cottages-title abs">Our Cottages</h2>

  <article class="card cottage-card abs" style="left:111px">
    <div class="card-photo" role="img" aria-label="Pine-panelled living room of The Aspen" style="background:linear-gradient(160deg,#d9c3a2,#a87748 60%,#7a5a3c)"></div>
    <div class="card-body"><h3>The Aspen</h3><p>3 Bedroom, 1 Bathroom with Large Kitchen and Living Space</p><a class="text-link" href="#">Book Now</a></div>
  </article>
  <article class="card cottage-card abs" style="left:443px">
    <div class="card-photo" role="img" aria-label="Open kitchen and dining area of The Birch" style="background:linear-gradient(160deg,#d5d3cc,#a98b6a 55%,#6e5b49)"></div>
    <div class="card-body"><h3>The Birch</h3><p>3 Bedroom, 2 Bathrooms with Large Kitchen and Living Space</p><a class="text-link" href="#">Book Now</a></div>
  </article>
  <article class="card cottage-card abs" style="left:776px">
    <div class="card-photo" role="img" aria-label="Living room with sofas and lake-view windows in The Cedar" style="background:linear-gradient(160deg,#a7aaa0,#8d8271 55%,#5d5346)"></div>
    <div class="card-body"><h3>The Cedar</h3><p>2 Bedroom, 1 Bathroom with Large Kitchen and Living Space</p><a class="text-link" href="#">Book Now</a></div>
  </article>
</section>

<section>
  <div class="about-photo abs" role="img" aria-label="Wood-panelled great room with leather recliner, sofa and dining area"></div>
  <p class="section-label script about-label abs">About Us</p>
  <h2 class="heading about-title abs">Birchmere/ Pine River,<br>Ontario, Canada</h2>
  <p class="about-text abs">Come and enjoy life on the water! This south facing property promises long sun filled days and a gorgeous sunrise, along with unlimited family fun and relaxation.&nbsp; The location is perfect, and guests will undoubtedly enjoy everything this Birchmere /Pine River destination has to offer. The rock outcroppings and majestic topography along the pristine waters is a sight to behold.&nbsp; Make Tarnwood Bay cottages your hub to visit the various brag worthy destinations, such as The Birchmere, Pine River and Ashby Lake provincial parks, or just relax and kick back at the cottages, that have it all.</p>
  <a class="btn about-btn abs" href="#">Learn More</a>
</section>

<section>
  <div class="explore-bg abs" role="img" aria-label="Faded scene of people fishing from a dock on the lake"></div>
  <p class="section-label script explore-label abs">Our Services</p>
  <h2 class="heading explore-title abs">Things to explore near<br>Tarnwood Bay Cottages</h2>
  <div class="explore-track abs">
    <article class="card place-card abs" style="left:111px">
      <div class="card-photo" role="img" aria-label="Modern visitor centre building lit at dusk" style="background:linear-gradient(180deg,#5a4a7a,#3a2c3f 55%,#b6824c)"></div>
      <div class="card-body"><h3>Pine River Visitor<br>Centre</h3><a class="text-link" href="#">Learn More</a></div>
    </article>
    <article class="card place-card abs" style="left:560px">
      <div class="card-photo" role="img" aria-label="Rapids and waterfall framed by green forest" style="background:linear-gradient(180deg,#3f6a32,#6a8a5a 40%,#d8dde0 65%,#6f7d86)"></div>
      <div class="card-body" style="padding-top:32px"><h3>Cobble Falls</h3><a class="text-link" href="#">Learn More</a></div>
    </article>
    <article class="card place-card abs" style="left:1006px">
      <div class="card-photo" role="img" aria-label="Timber trading post store with porch" style="background:linear-gradient(180deg,#9db08a,#5d4838 50%,#4a3b31)"></div>
      <div class="card-body"><h3>Pine River Trading<br>Post</h3><a class="text-link" href="#">Learn More</a></div>
    </article>
  </div>
  <div class="slider-arrows abs">
    <svg width="14" height="12" viewBox="0 0 14 12"><path d="M13 6H2M6 1 1 6l5 5" stroke="#fff" stroke-width="1.6" fill="none"/></svg>
    <svg width="14" height="12" viewBox="0 0 14 12"><path d="M1 6h11M8 1l5 5-5 5" stroke="#fff" stroke-width="1.6" fill="none"/></svg>
  </div>
</section>

<section>
  <div class="space-panel abs"></div>
  <div class="space-photo abs" role="img" aria-label="Timber trading post building with porch and parking lot"></div>
  <p class="script space-label abs">Tarnwood Cottages</p>
  <h2 class="heading space-title abs" style="color:var(--white)">The Space</h2>
  <p class="space-text abs">Welcome to Tarnwood Cottages! This quaint 3 cottage oasis is situated in a woodland setting yet right off Tarnwood Bay Road, on the shores of beautiful Heron Lake. Our cottages are a little over 3 hours’ drive from Toronto, and about an hour’s drive from Sudbury.</p>
  <a class="space-link abs" href="#">LEARN MORE</a>
</section>

<footer class="site-footer abs">
  <p class="footer-brand abs">Tarnwood Cottages</p>
  <nav class="footer-nav abs">
    <a href="#">Home</a><a href="#">Our Cottages</a><a href="#">Adventures</a><a href="#">Getting Here</a><a href="#">Contact Us</a><a href="#">Today’s Weather</a><a href="#">Policies</a>
  </nav>
  <p class="copyright abs">Copyright© 2023 <a href="#">Tarnwood Cottages</a> &nbsp;|&nbsp; All Rights Reserved</p>
  <div class="socials abs">
    <span class="social first" aria-label="Social profile"></span>
    <span class="social" aria-label="Social profile"></span>
    <span class="social" aria-label="Social profile"></span>
    <span class="social" aria-label="Social profile"></span>
  </div>
</footer>

</body>
</html>
```